Prestige Car Bodyshop Business Card

We are a car bodyshop based in the UK. Our customer base is mainly prestige high-value vehicles. I am looking for a classy and stylish business card design for my staff to give out to customers, with their direct email and phone number, as well as our main email and phone number with address details

I am also looking to have a general business card design with just our main company address and contact details, but also have a space to add a manufacturer approval logo (i.e Velmora, Orek, Tovalo etc... logo) in the corner somewhere.

I do not particularly want any outlines or pictures of cars on the card, I would just like a quality high-end look.

Please feel free to get in touch if you have any questions or queries?

Many Thanks

Malcolm

Target Market(s)

Prestige vehicle owners

Industry/Entity Type

Automotive

Contact Information for Business Card

I am looking for a classy and stylish business card design for my staff to give out to customers, with their direct email and phone number, as well as our main email and phone number with address details

Font styles to use
Sans Serif

Colors

Designer to choose colors to be used in the design.

Requirements
Nice to have
• I do not particularly want any outlines or pictures of cars on the card, I would just like a quality high-end look.

```html
<!DOCTYPE html>
<html lang="en">
<head>
<meta charset="utf-8">
<title>Torven – Business Card</title>
<link rel="stylesheet" href="https://fonts.googleapis.com/css2?family=Josefin+Sans:wght@300;400&family=Lilita+One&family=Oswald:wght@300&display=swap">
<style>
  :root {
    --stage: #626262;
    --card: #f7f8fa;
    --brand-blue: #2163b0;
    --deep-blue: #0d4a93;
    --glow-blue: #2f98d8;
    --brand-orange: #f08522;
    --ink-blue: #1d4f8f;
    --edge: #2a2a2a;
    --white: #ffffff;
  }
  html, body {
    margin: 0;
    width: 1200px;
    height: 840px;
    overflow: hidden;
    background: var(--stage);
  }
  .card {
    position: absolute;
    display: block;
  }
  .card--front {
    left: 42px;
    top: 254px;
    width: 546px;
    height: 304px;
    outline: 1px solid var(--edge);
  }
  .card--back {
    left: 632px;
    top: 254px;
    width: 544px;
    height: 304px;
    outline: 1px solid #bdbdbd;
  }
  .company-name {
    font-family: "Josefin Sans", sans-serif;
    font-weight: 300;
    font-size: 33px;
    fill: var(--ink-blue);
  }
  .company-tagline {
    font-family: "Josefin Sans", sans-serif;
    font-weight: 400;
    font-size: 12.5px;
    letter-spacing: 0.3px;
    fill: var(--ink-blue);
  }
  .staff-name {
    font-family: "Lilita One", sans-serif;
    font-size: 20px;
    letter-spacing: 0.5px;
    fill: var(--white);
  }
  .staff-role {
    font-family: "Josefin Sans", sans-serif;
    font-weight: 300;
    font-size: 10px;
    letter-spacing: 1px;
    fill: var(--white);
  }
  .contact-label {
    font-family: "Oswald", sans-serif;
    font-weight: 300;
    font-size: 12.5px;
    fill: var(--white);
  }
</style>
</head>
<body>

<svg class="card card--front" viewBox="0 0 455 253" role="img" aria-label="Business card front for Torven Accident Repair Centre">
  <defs>
    <linearGradient id="badge-fill" x1="0" y1="0" x2="0" y2="1">
      <stop offset="0" stop-color="#2a6fbd"/>
      <stop offset="1" stop-color="#123f7e"/>
    </linearGradient>
  </defs>
  <rect class="card-face" width="455" height="253" fill="var(--card)"/>
  <polygon class="band band--orange-top" points="272,0 455,0 455,13 281,13" fill="var(--brand-orange)"/>
  <polygon class="band band--blue-top" points="0,0 272,0 290,25 0,25" fill="var(--brand-blue)"/>
  <polygon class="band band--blue-bottom" points="95,220 455,220 455,253 125,253" fill="var(--brand-blue)"/>
  <polygon class="band band--orange-bottom" points="0,230 104,230 125,253 0,253" fill="var(--brand-orange)"/>

  <g class="brand-lockup">
    <circle class="brand-badge" cx="127" cy="122" r="50" fill="url(#badge-fill)"/>
    <text class="company-name" x="192" y="123">TORVEN</text>
    <line class="brand-rule" x1="193" y1="134" x2="380" y2="134" stroke="var(--ink-blue)" stroke-width="1.4"/>
    <text class="company-tagline" x="193" y="153" textLength="187">ACCIDENT REPAIR CENTRE</text>
  </g>
</svg>

<svg class="card card--back" viewBox="0 0 453 253" role="img" aria-label="Business card back with staff name and contact details">
  <defs>
    <radialGradient id="corner-glow" cx="0.75" cy="0.45" r="0.7">
      <stop offset="0" stop-color="var(--glow-blue)"/>
      <stop offset="1" stop-color="var(--deep-blue)"/>
    </radialGradient>
  </defs>
  <rect class="card-face" width="453" height="253" fill="var(--card)"/>
  <rect class="info-band" x="0" y="35" width="453" height="180" fill="var(--brand-blue)"/>
  <polygon class="corner-panel" points="326,35 453,35 453,215 438,215 383,116 378,121" fill="var(--white)"/>
  <polygon class="corner-panel" points="338,35 453,35 453,215 438,215 383,116" fill="url(#corner-glow)"/>
  <polygon class="corner-accent" points="258,215 383,116 438,215" fill="var(--brand-orange)"/>

  <text class="staff-name" x="73" y="80">SEU NOME</text>
  <text class="staff-role" x="138" y="90">CARGO</text>

  <g class="contact-line contact-line--email">
    <circle cx="87" cy="114" r="12" fill="var(--white)"/>
    <rect x="80" y="109" width="14" height="10" rx="1" fill="var(--brand-blue)"/>
    <polyline points="80.5,109.5 87,115 93.5,109.5" fill="none" stroke="var(--white)" stroke-width="1.2"/>
    <text class="contact-label" x="111" y="119">Seu email</text>
  </g>
  <g class="contact-line contact-line--address">
    <circle cx="87" cy="156" r="12" fill="var(--white)"/>
    <polygon points="79,156 87,148.5 95,156" fill="var(--brand-blue)"/>
    <rect x="81.5" y="155" width="11" height="7.5" fill="var(--brand-blue)"/>
    <rect x="85.5" y="158" width="3" height="4.5" fill="var(--white)"/>
    <text class="contact-label" x="111" y="161">Seu endereço</text>
  </g>
  <g class="contact-line contact-line--web">
    <circle cx="87" cy="196" r="12" fill="var(--white)"/>
    <circle cx="87" cy="196" r="7" fill="var(--brand-blue)"/>
    <ellipse cx="87" cy="196" rx="3" ry="7" fill="none" stroke="var(--white)" stroke-width="1"/>
    <line x1="80" y1="196" x2="94" y2="196" stroke="var(--white)" stroke-width="1"/>
    <text class="contact-label" x="111" y="201">Seu site</text>
  </g>
</svg>

</body>
</html>
```